Business card for Chiropractic clinics needs reworked / redesigned

The business card in attachment was designed 10 years ago. It is in need of an update.
We have 2 clinics:
VELDHOVE KLINIEK & VELDHOVE KLINIEK NOORD
Only one address needs to be on the card for doctors that only work in one clinic and two addresses need to be on the card for the doctors that work in both clinics.

Target Market(s)

patients/referrers

Industry/Entity Type

Medical

Contact Information for Business Card

Logo (in full or zoomed-in)
Clinic Name
Doctor name and title
clinic address, website, tel, email

Font styles to use
Sans Serif

Colors

Designer to choose colors to be used in the design.

Requirements
Must have
• Good contrast/readability
• We like modern minimalistic designs
• The Bcard needs to project our very high standard of proficiency/professionalism
Should not have
• Not curly
• Not to much colours

```html
<!DOCTYPE html>
<html lang="nl">
<head>
<meta charset="utf-8">
<title>Veldhove Kliniek – visitekaartje</title>
<link rel="stylesheet" href="https://fonts.googleapis.com/css2?family=Figtree:wght@400;500;600&display=swap">
<style>
  :root {
    --ink: #0b2325;
    --paper: #ffffff;
    --swoosh: #8c8c8c;
    --backdrop: #3a3a3a;
    --text-light: #ffffff;
  }
  html, body {
    margin: 0;
    padding: 0;
    width: 1200px;
    height: 960px;
    overflow: hidden;
    background: var(--backdrop);
    font-family: "Figtree", Arial, sans-serif;
  }
  .stage {
    position: relative;
    width: 1200px;
    height: 960px;
  }
  .card {
    position: absolute;
    left: 240px;
    width: 720px;
    height: 411px;
    border-radius: 20px;
    overflow: hidden;
    box-shadow: 0 8px 22px rgba(0,0,0,0.35);
  }
  .card--front { top: 41px; background: var(--paper); }
  .card--back  { top: 508px; background: var(--ink); }
  .card__shape {
    position: absolute;
    inset: 0;
    width: 720px;
    height: 411px;
  }
  .front-brand {
    position: absolute;
    left: 0;
    width: 330px;
    top: 190px;
    text-align: center;
    color: var(--ink);
    font-weight: 600;
    font-size: 22px;
    letter-spacing: 0.5px;
  }
  .contact {
    position: absolute;
    left: 446px;
    top: 96px;
    color: var(--text-light);
  }
  .contact__name {
    margin: 0;
    font-size: 24px;
    font-weight: 600;
  }
  .contact__title {
    margin: 4px 0 0;
    font-size: 17px;
    font-weight: 400;
  }
  .contact__list {
    list-style: none;
    margin: 22px 0 0;
    padding: 0;
    font-size: 15.5px;
    line-height: 24px;
  }
  .contact__item {
    display: flex;
    align-items: flex-start;
  }
  .contact__item--gap { margin-top: 14px; }
  .contact__icon {
    width: 12px;
    height: 12px;
    margin: 6px 12px 0 0;
    flex: none;
  }
  .back-mark {
    position: absolute;
    left: 150px;
    top: 175px;
    width: 60px;
    height: 60px;
    border-radius: 50%;
    background: var(--text-light);
  }
  .back-brand {
    position: absolute;
    left: 240px;
    width: 370px;
    top: 173px;
    text-align: center;
    color: var(--text-light);
  }
  .back-brand__name {
    margin: 0;
    font-size: 26px;
    font-weight: 600;
    letter-spacing: 0.3px;
  }
  .back-brand__web {
    margin: 4px 0 0;
    font-size: 15.5px;
  }
</style>
</head>
<body>
<main class="stage">

  <section class="card card--front">
    <svg class="card__shape" viewBox="0 0 720 411" aria-hidden="true">
      <path fill="var(--swoosh)" d="M360 0 C314 42 304 122 336 202 C368 282 382 342 352 411 L368 411 C398 340 384 280 352 200 C320 120 330 42 372 0 Z"/>
      <path fill="var(--ink)" d="M374 0 C332 42 322 122 354 202 C386 282 400 342 370 411 L720 411 L720 0 Z"/>
    </svg>

    <div class="front-brand">VELDHOVE KLINIEK</div>

    <div class="contact">
      <h1 class="contact__name">Lars Verhoeven</h1>
      <p class="contact__title">President &amp; CEO</p>
      <ul class="contact__list">
        <li class="contact__item">
          <svg class="contact__icon" viewBox="0 0 12 12" aria-hidden="true"><path fill="#fff" d="M6 0a4 4 0 0 1 4 4c0 3-4 8-4 8S2 7 2 4a4 4 0 0 1 4-4zm0 2.4a1.6 1.6 0 1 0 0 3.2 1.6 1.6 0 0 0 0-3.2z"/></svg>
          <span>VELDHOVE KLINIEK<br>Lindenlaan 148</span>
        </li>
        <li class="contact__item contact__item--gap">
          <svg class="contact__icon" viewBox="0 0 12 12" aria-hidden="true"><path fill="none" stroke="#fff" stroke-width="1.6" stroke-linecap="round" d="M3 1.5 C1 3 1 7 4 9.5 C6.5 11.5 9 11.5 10.5 10 M3 1.5 L4.5 4 M10.5 10 L8 8.5"/></svg>
          <span>+32 9 555 01 84</span>
        </li>
        <li class="contact__item">
          <svg class="contact__icon" viewBox="0 0 12 12" aria-hidden="true"><rect x="0.5" y="2.5" width="11" height="7" fill="#fff"/><path fill="none" stroke="var(--ink)" stroke-width="1" d="M0.5 2.5 L6 6.5 L11.5 2.5"/></svg>
          <span>info@veldhovekliniek.be</span>
        </li>
        <li class="contact__item">
          <svg class="contact__icon" viewBox="0 0 12 12" aria-hidden="true"><g fill="none" stroke="#fff" stroke-width="1"><circle cx="6" cy="6" r="5"/><ellipse cx="6" cy="6" rx="2.2" ry="5"/><path d="M1 6h10M2 3.3h8M2 8.7h8"/></g></svg>
          <span>www.veldhovekliniek.be</span>
        </li>
      </ul>
    </div>
  </section>

  <section class="card card--back">
    <div class="back-mark" aria-hidden="true"></div>
    <div class="back-brand">
      <h2 class="back-brand__name">VELDHOVE KLINIEK</h2>
      <p class="back-brand__web">www.veldhovekliniek.be</p>
    </div>
  </section>

</main>
</body>
</html>
```